Business card for different employees

A professional new updated design incorporating our current business's color themes and styles such as our on-site service trucks decals included in pictures attached. Our current business card is very simple and not professionally designed. We are a small family business but want a professional corporate look.

Target Market(s)

Cards to be handed out to new customers , corperate meetings. For our on site service operators.

Industry/Entity Type

Hydraulic

Contact Information for Business Card

Address, website, phone number, email, logo.
slogan - "Industry chosen hose and fittings provider".
24/7 on-site service , supply and hose management
Experienced , indpendant , family owned

Font styles to use
Sans Serif

Requirements
Must have
• Easily editable so that I can add different names and different roles for employees etc.
Nice to have
• Freedom with colour doesn't necessarily have to be blue but that is our company colour theme with trucks and logo so makes sense for the card to have blue like the trucks.

```html
<!DOCTYPE html>
<html lang="en">
<head>
<meta charset="utf-8">
<title>Corvane Hose &amp; Fittings – Business Card</title>
<link rel="stylesheet" href="https://fonts.googleapis.com/css2?family=Roboto:wght@300;400;700&display=swap">
<style>
  :root {
    --brand-blue: #2d43a0;
    --brand-blue-deep: #1f2f7a;
    --brand-blue-light: #3a52b6;
    --ink: #1b1b1b;
    --ink-soft: #2a2a2a;
    --band-black: #151515;
    --paper: #ffffff;
    --icon-grey: #b9b9bd;
  }
  html, body {
    margin: 0;
    width: 1200px;
    height: 1200px;
    overflow: hidden;
    background: var(--paper);
  }
  .canvas {
    position: relative;
    width: 1200px;
    height: 1200px;
  }
  .business-card {
    position: absolute;
    left: 55px;
    top: 252px;
    width: 1090px;
    height: 695px;
    font-family: "Roboto", sans-serif;
  }
  .company-name { font-weight: 700; fill: var(--brand-blue); letter-spacing: 0.5px; }
  .person-name { font-weight: 400; fill: var(--ink); }
  .person-title { font-weight: 400; fill: var(--brand-blue); }
  .person-department { font-weight: 300; fill: var(--ink-soft); }
  .contact-value { font-weight: 700; fill: var(--paper); }
  .contact-note { font-weight: 400; fill: var(--paper); }
  .contact-note-label { font-weight: 700; }
</style>
</head>
<body>
<main class="canvas">
  <svg class="business-card" viewBox="0 0 623 397" xmlns="http://www.w3.org/2000/svg" aria-label="Business card for Marlo Tenbrook, Corvane Hose &amp; Fittings">
    <defs>
      <linearGradient id="panel-gradient" x1="0" y1="0" x2="1" y2="0">
        <stop offset="0" stop-color="var(--brand-blue-light)"/>
        <stop offset="0.75" stop-color="var(--brand-blue)"/>
        <stop offset="1" stop-color="var(--brand-blue-deep)"/>
      </linearGradient>
    </defs>

    <!-- card base -->
    <rect class="card-face" width="623" height="397" fill="var(--paper)"/>

    <!-- left brand panel -->
    <polygon class="brand-panel" points="0,0 133,0 272,380 0,380" fill="url(#panel-gradient)"/>
    <polygon class="brand-panel-edge" points="120,0 133,0 272,380 250,380" fill="var(--brand-blue-deep)" opacity="0.55"/>

    <!-- bottom band -->
    <rect class="footer-band" x="0" y="380" width="623" height="17" fill="var(--band-black)"/>

    <!-- brand mark area -->
    <circle class="brand-dot" cx="85" cy="79" r="58" fill="var(--band-black)"/>
    <text class="company-name" x="178" y="86" font-size="28">CORVANE HOSE &amp; FITTINGS</text>

    <!-- person -->
    <text class="person-name" x="588" y="166" font-size="34" text-anchor="end">MARLO TENBROOK</text>
    <text class="person-title" x="590" y="195" font-size="21" text-anchor="end">Director</text>
    <text class="person-department" x="590" y="217" font-size="17" text-anchor="end">Business Devlopment &amp; Research</text>

    <!-- contact tabs -->
    <g class="contact-list">
      <g class="contact-row contact-email">
        <polygon points="202,254 452,254 452,277 212,277" fill="var(--brand-blue)"/>
        <rect x="440" y="254" width="37" height="23" rx="11.5" fill="var(--band-black)"/>
        <circle cx="436" cy="265.5" r="3.5" fill="none" stroke="var(--band-black)" stroke-width="1.5"/>
        <g fill="none" stroke="var(--paper)" stroke-width="1.2">
          <rect x="453" y="261" width="13" height="9"/>
          <polyline points="453,261 459.5,266.5 466,261"/>
        </g>
        <text class="contact-value" x="422" y="270" font-size="12" text-anchor="end">marlo@corvanehose.com</text>
      </g>
      <g class="contact-row contact-phone">
        <polygon points="210,284 452,284 452,307 218,307" fill="var(--brand-blue)"/>
        <rect x="440" y="284" width="37" height="23" rx="11.5" fill="var(--band-black)"/>
        <circle cx="436" cy="295.5" r="3.5" fill="none" stroke="var(--band-black)" stroke-width="1.5"/>
        <rect x="455" y="288" width="8" height="15" rx="1.5" fill="none" stroke="var(--paper)" stroke-width="1.2"/>
        <rect x="457" y="290.5" width="4" height="6" fill="var(--paper)"/>
        <text class="contact-value" x="422" y="300" font-size="12" text-anchor="end">0298765432</text>
      </g>
      <g class="contact-row contact-fax">
        <polygon points="210,315 452,315 452,338 218,338" fill="var(--brand-blue)"/>
        <rect x="440" y="315" width="37" height="23" rx="11.5" fill="var(--band-black)"/>
        <circle cx="436" cy="326.5" r="3.5" fill="none" stroke="var(--band-black)" stroke-width="1.5"/>
        <g fill="none" stroke="var(--paper)" stroke-width="1.2">
          <rect x="455" y="318.5" width="8" height="4"/>
          <rect x="452" y="322.5" width="14" height="7" rx="1"/>
          <rect x="455" y="327" width="8" height="5"/>
        </g>
        <text class="contact-value" x="422" y="331" font-size="12" text-anchor="end">0298765432</text>
      </g>
      <g class="contact-row contact-web">
        <polygon points="210,344 452,344 452,367 218,367" fill="var(--brand-blue)"/>
        <rect x="440" y="344" width="37" height="23" rx="11.5" fill="var(--band-black)"/>
        <circle cx="436" cy="355.5" r="3.5" fill="none" stroke="var(--band-black)" stroke-width="1.5"/>
        <g fill="none" stroke="var(--paper)" stroke-width="1.1">
          <circle cx="459" cy="355.5" r="6.5"/>
          <ellipse cx="459" cy="355.5" rx="3" ry="6.5"/>
          <line x1="452.5" y1="355.5" x2="465.5" y2="355.5"/>
        </g>
        <text class="contact-value" x="422" y="360" font-size="12" text-anchor="end">www.corvanehose.com</text>
      </g>
    </g>

    <!-- social placeholders -->
    <g class="social-links" fill="var(--icon-grey)">
      <rect x="27" y="284" width="23" height="23" rx="4"/>
      <rect x="64" y="284" width="23" height="23" rx="4"/>
      <rect x="102" y="284" width="23" height="23" rx="4"/>
      <rect x="140" y="284" width="23" height="23" rx="4"/>
    </g>

    <!-- contact note -->
    <text class="contact-note" font-size="11.2">
      <tspan x="28" y="332"><tspan class="contact-note-label">Contact:</tspan> Lorem Ipsum is simply</tspan>
      <tspan x="28" y="347" textLength="186" lengthAdjust="spacing">dummy text of the printing and</tspan>
      <tspan x="28" y="362" textLength="186" lengthAdjust="spacing">typesetting industry. Lorem Ipsum</tspan>
    </text>
  </svg>
</main>
</body>
</html>
```